Business Card For Video Production Company

Please NOTE: I've added some info to the must haves that I should have included at the start. Thank you.

I need a business card design for my video production company based in Orlando called Caldera Film Works. Our work consists of web video marketing (web videos), training videos, sales videos, conference and seminar video production...basically a lot of corporate based work.

We work with successful small businesses, not-for-profits and some Fortune 500 type groups. We bring a lot of knowledge, experience and attention to detail to every project.

I'd like something that communicates strength, confidence, integrity, as well as creative vision. I want to stay away from the standard icons of the media and film industry. I'd like to emphasize the colors of my logo, and also the colors of my website which has a white background. Simple is good.

Our budgets are moderate...generally $1500 to $5000.

www.calderafilm.tv

PS...We don't do weddings or recitals, or that type of production.
Updates

I want to thank all the designers for your updates. There's way too many to be able to give feedback on for all. I hope you understand that. But wow…there are so many great designs everyone has offered. I can't thank you enough…each and everyone. I hope to make my decision soon. I'm not accepting anymore designs from new designers. Brent-

Target Market(s)

Successful small businesses, marketing directors, corporate communication directors, training and human resources professionals. forward thinking not-for profits. Since my company is based in Central Florida, most of my work comes from this area too.

Industry/Entity Type

Marketing

Requirements
Must have
• website address, www.calderafilm.tv
phone number, 407-552-9031
email address, brent@calderafilm.tv

Title
Brent Caldera
Owner/Creative Director

I'd like to have a single line that goes across illustrating our services, maybe separated with bullet points:

Marketing Videos, Corporate Videos, Conference & Seminar Video Production
Should not have
• No film or video icons.
No need to pull language or copy from my website.

```html
<!DOCTYPE html>
<html lang="en">
<head>
<meta charset="utf-8">
<title>Caldera Film Works – Business Card</title>
<link rel="stylesheet" href="https://fonts.googleapis.com/css2?family=Montserrat:wght@700&family=Arimo:wght@400;700&family=Lato:wght@300;400&display=swap">
<style>
  :root {
    --backdrop: #2b2b2d;
    --card-white: #ffffff;
    --card-charcoal: #555558;
    --ink-dark: #4a4a4d;
    --ink-mid: #5c5c60;
    --ink-light: #e6e6e8;
    --brand-blue: #0a8fd8;
    --brand-sky: #8fd3f5;
    --band-grey: #5a5a5e;
  }
  * { box-sizing: border-box; margin: 0; padding: 0; }
  html, body {
    width: 1200px; height: 900px; overflow: hidden;
    background: var(--backdrop);
  }
  .canvas { position: relative; width: 1200px; height: 900px; }

  .card {
    position: absolute;
    width: 630px; height: 360px;
    overflow: hidden;
    box-shadow: 0 18px 40px rgba(0,0,0,.45);
  }

  /* Front */
  .card-front { left: 60px; top: 60px; background: var(--card-white); }
  .brand {
    position: absolute; left: 56px; top: 74px;
    display: flex; align-items: center; gap: 16px;
  }
  .brand-square { width: 44px; height: 44px; background: var(--brand-blue); }
  .brand-name {
    font-family: "Montserrat", sans-serif; font-weight: 700;
    font-size: 34px; color: var(--ink-dark); letter-spacing: -0.5px;
    white-space: nowrap;
  }
  .person { position: absolute; left: 56px; top: 164px; font-family: "Arimo", sans-serif; }
  .person-name { font-weight: 700; font-size: 25px; color: var(--ink-dark); }
  .person-title { font-size: 17px; color: var(--ink-mid); margin-top: 2px; }
  .contact-list { list-style: none; margin-top: 18px; }
  .contact-list li {
    display: flex; align-items: center; gap: 14px;
    font-size: 17px; color: var(--ink-mid); line-height: 28px;
    white-space: nowrap;
  }
  .contact-list svg { width: 16px; height: 16px; flex: none; }

  .band-grey { position: absolute; left: 0; bottom: 0; width: 420px; height: 30px; background: var(--band-grey); }
  .band-blue { position: absolute; left: 420px; bottom: 0; width: 150px; height: 44px; background: var(--brand-blue); }
  .band-sky  { position: absolute; left: 570px; bottom: 0; width: 60px;  height: 58px; background: var(--brand-sky); }

  /* Back */
  .card-back { left: 510px; top: 480px; background: var(--card-charcoal); }
  .card-back .brand { left: 64px; top: 96px; }
  .card-back .brand-name { color: var(--card-white); }
  .services {
    position: absolute; left: 28px; right: 28px; bottom: 38px;
    font-family: "Lato", sans-serif; font-weight: 300;
    font-size: 15px; color: var(--ink-light);
    white-space: nowrap; text-align: center;
  }
</style>
</head>
<body>
<main class="canvas">

  <section class="card card-front" aria-label="Business card front">
    <div class="brand">
      <span class="brand-square"></span>
      <span class="brand-name">Caldera Film Works</span>
    </div>

    <div class="person">
      <p class="person-name">Brent Caldera</p>
      <p class="person-title">Owner/Creative Director</p>
      <ul class="contact-list">
        <li>
          <svg viewBox="0 0 16 16" aria-hidden="true"><path fill="#0a8fd8" d="M3.6 1.5l2.3 2.6-1.3 1.8c.9 2 2.4 3.6 4.5 4.6l1.8-1.3 2.6 2.3-1.4 2.3C7.2 13.6 2.4 8.8 1.2 3z"/></svg>
          407-552-9031
        </li>
        <li>
          <svg viewBox="0 0 16 16" aria-hidden="true"><rect x="1" y="3" width="14" height="10" fill="#0a8fd8"/><path d="M1.5 3.5L8 9l6.5-5.5" stroke="#fff" stroke-width="1.3" fill="none"/></svg>
          brent@calderafilm.tv
        </li>
        <li>
          <svg viewBox="0 0 16 16" aria-hidden="true"><circle cx="8" cy="8" r="7" fill="#0a8fd8"/><path d="M1 8h14M8 1c-3 3.5-3 10.5 0 14M8 1c3 3.5 3 10.5 0 14" stroke="#fff" stroke-width="1" fill="none"/></svg>
          www.calderafilm.tv
        </li>
      </ul>
    </div>

    <div class="band-grey"></div>
    <div class="band-blue"></div>
    <div class="band-sky"></div>
  </section>

  <section class="card card-back" aria-label="Business card back">
    <div class="brand">
      <span class="brand-square"></span>
      <span class="brand-name">Caldera Film Works</span>
    </div>
    <p class="services">Marketing Videos | Corporate Videos | Conference &amp; Seminar Video Production</p>
  </section>

</main>
</body>
</html>
```